PLUME Residence One-Page Inserts

We need TWO one-page insert for a transplant display stand (6"x8"). We have a few furnished apartments and we need to inform our guests about the services available:

Insert #1: Delivery and Pickup Services in the neighborhood (Laundry, Groceries, Restaurants).
Insert #1 Text: "Heading: Pick and Delivery Services in your neighborhood:" Text below it: "1) Laundry Pickup - Call: +9714-382-7160. 2) Groceries Delivery - Call: +9714-382-7160, 3) Restaurants Delivery - Call: +9714-382-7160"

Insert #2: We also need another one-page insert to encourage the guests to enjoy the candles and to make the apartment have a homier feeling.
Insert #2 Text: "Heading: Feel at home. Text below it: "Dim the lights, light up a candle, play nice music, have a relaxing stay."

Target Market(s)

Staybrook Users. Apartment Guests. Tourist. Age Group 20 to 60 years old.

Industry/Entity Type

Hotel

Requirements
Must have
• - The Company logo of PLUME Residence must be displayed on the upper corner. (Logo attached). The logo should be a single color either white or black (Not red and black or red and white)
• For Insert # 1: Laundry, Groceries, and Breakfast Resturaunts images or icons. The images/icons must be unified and look like from the same family of images/icons.
• For Insert # 2: A romantic candle(s) dinner pictures.
Nice to have
• Not too many colors
• Not too busy
• Simple
• Eye Catchy
Should not have
• Lots of colors
• Too many images
• Too Busy

```html
<!DOCTYPE html>
<html lang="en">
<head>
<meta charset="utf-8">
<title>PLUME Residence Inserts</title>
<link href="https://fonts.googleapis.com/css2?family=Montserrat:wght@400;500;600;700;800&display=swap" rel="stylesheet">
<style>
  :root {
    --stage: #c4c4c4;
    --paper-white: #ffffff;
    --paper-fade: #ececec;
    --ink: #1f1f1f;
    --maroon: #7e1c1c;
    --navy: #1b3c6e;
    --green: #1f7a2c;
    --cream-1: #f3efe6;
    --cream-2: #ddd5c4;
    --kraft-1: #c9a679;
    --kraft-2: #a8845a;
    --spa-light: #b59a82;
    --spa-mid: #6e5a4b;
    --spa-dark: #2e2520;
  }
  * { margin: 0; padding: 0; box-sizing: border-box; }
  html, body { width: 1200px; height: 1005px; overflow: hidden; }
  body {
    background: var(--stage);
    font-family: "Montserrat", Arial, sans-serif;
    color: var(--ink);
    position: relative;
  }
  .insert {
    position: absolute;
    width: 544px;
    height: 724px;
    overflow: hidden;
    box-shadow: 0 6px 24px rgba(0,0,0,0.35);
  }
  .insert--services {
    left: 43px; top: 154px;
    background: radial-gradient(ellipse at 60% 35%, var(--paper-white) 40%, var(--paper-fade) 100%);
  }
  .insert--home {
    left: 609px; top: 131px;
    background: radial-gradient(ellipse at 60% 30%, var(--cream-1) 30%, var(--cream-2) 100%);
  }
  .brand-name {
    position: absolute;
    left: 0; right: 0;
    text-align: center;
    font-weight: 500;
    font-size: 60px;
    line-height: 1;
    color: var(--ink);
  }
  .insert--services .brand-name { top: 48px; }
  .insert--home .brand-name { top: 49px; }

  .services-heading {
    position: absolute;
    top: 141px; left: 0; width: 100%;
    text-align: center;
    font-size: 44px;
    line-height: 53px;
    font-weight: 500;
  }
  .services-heading .accent { color: var(--maroon); font-weight: 700; }
  .services-heading .lead { font-weight: 600; }

  .service {
    position: absolute;
    left: 155px;
    display: flex;
    align-items: center;
  }
  .service__icon { width: 80px; height: 80px; flex: none; }
  .service__text { margin-left: 14px; }
  .service__name { font-size: 24px; font-weight: 600; line-height: 28px; }
  .service__call { font-size: 25px; font-weight: 800; line-height: 31px; white-space: nowrap; }
  .service__call small { font-size: 17px; font-weight: 700; }
  .service--laundry { top: 337px; }
  .service--laundry .service__name { color: var(--navy); }
  .service--groceries { top: 436px; }
  .service--groceries .service__name { color: var(--green); }
  .service--restaurants { top: 543px; }
  .service--restaurants .service__name { color: var(--maroon); }

  .photo-bag {
    position: absolute; left: 0; top: 390px; width: 125px; height: 334px;
    background: linear-gradient(90deg, var(--kraft-2), var(--kraft-1));
  }
  .photo-cup {
    position: absolute; left: 105px; top: 582px; width: 100px; height: 142px;
    background: linear-gradient(180deg, #ecebe6 0%, #c2a276 30%, #a98658 100%);
  }

  .home-heading {
    position: absolute;
    left: 125px; top: 150px;
    font-size: 54px;
    line-height: 64px;
    font-weight: 700;
    letter-spacing: -0.5px;
    white-space: nowrap;
  }
  .home-rule {
    position: absolute;
    left: 125px; right: 0; top: 210px;
    height: 3px;
    background: var(--maroon);
  }
  .home-copy {
    position: absolute;
    left: 125px; top: 235px;
    font-size: 24px;
    line-height: 36.5px;
    font-weight: 500;
    white-space: nowrap;
  }
  .photo-spa {
    position: absolute;
    left: 0; right: 0; top: 430px; bottom: 0;
    background: linear-gradient(180deg, var(--spa-light) 0%, var(--spa-mid) 55%, var(--spa-dark) 100%);
  }
</style>
</head>
<body>

  <section class="insert insert--services">
    <div class="brand-name">PLUME</div>
    <h1 class="services-heading">
      <span class="accent">Pick</span> <span class="lead">and</span> <span class="accent">Delivery</span><br>
      Services in your<br>neighborhood
    </h1>

    <div class="photo-bag" role="img" aria-label="Paper grocery bag photo"></div>
    <div class="photo-cup" role="img" aria-label="Takeaway coffee cup photo"></div>

    <div class="service service--laundry">
      <svg class="service__icon" viewBox="0 0 80 80" aria-hidden="true">
        <circle cx="40" cy="40" r="38" fill="#fff" stroke="var(--navy)" stroke-width="3"/>
        <rect x="24" y="20" width="30" height="40" rx="3" fill="var(--navy)"/>
        <rect x="27" y="23" width="24" height="5" fill="#fff"/>
        <circle cx="39" cy="44" r="10" fill="#fff"/>
        <circle cx="39" cy="44" r="6" fill="var(--navy)"/>
        <circle cx="60" cy="38" r="3" fill="none" stroke="var(--navy)" stroke-width="1.5"/>
        <circle cx="62" cy="45" r="2.5" fill="none" stroke="var(--navy)" stroke-width="1.5"/>
      </svg>
      <div class="service__text">
        <div class="service__name">Laundry Pickup</div>
        <div class="service__call"><small>Call:</small> +9714-382-7160</div>
      </div>
    </div>

    <div class="service service--groceries">
      <svg class="service__icon" viewBox="0 0 80 80" aria-hidden="true">
        <circle cx="40" cy="40" r="38" fill="#fff" stroke="var(--green)" stroke-width="3"/>
        <path d="M18 24h7l6 24h22l5-18H28" fill="none" stroke="var(--green)" stroke-width="4" stroke-linejoin="round"/>
        <path d="M30 36h26M32 42h22M39 30v18M47 30v18" stroke="var(--green)" stroke-width="2.5"/>
        <circle cx="34" cy="56" r="4" fill="var(--green)"/>
        <circle cx="50" cy="56" r="4" fill="var(--green)"/>
      </svg>
      <div class="service__text">
        <div class="service__name">Groceries Delivery</div>
        <div class="service__call"><small>Call:</small> +9714-382-7160</div>
      </div>
    </div>

    <div class="service service--restaurants">
      <svg class="service__icon" viewBox="0 0 80 80" aria-hidden="true">
        <circle cx="40" cy="40" r="38" fill="#fff" stroke="var(--maroon)" stroke-width="3"/>
        <path d="M22 58L52 24" stroke="var(--maroon)" stroke-width="5" stroke-linecap="round"/>
        <path d="M24 22l34 36" stroke="var(--maroon)" stroke-width="5" stroke-linecap="round"/>
        <path d="M52 16l6 6M56 13l6 6M60 10l5 5" stroke="var(--maroon)" stroke-width="2.5" stroke-linecap="round"/>
      </svg>
      <div class="service__text">
        <div class="service__name">Restaurants Delivery</div>
        <div class="service__call"><small>Call:</small> +9714-382-7160</div>
      </div>
    </div>
  </section>

  <section class="insert insert--home">
    <div class="photo-spa" role="img" aria-label="Photo of lit candles beside rolled white towels and pink orchids"></div>
    <div class="brand-name">PLUME</div>
    <h1 class="home-heading">Feel at home.</h1>
    <div class="home-rule"></div>
    <p class="home-copy">Dim the lights, light up a<br>candle, play nice music,<br>have a relaxing stay.</p>
  </section>

</body>
</html>
```